Algae Cream Package Concept

Creative Brief — Solvane: Phytoplankton Rescue Cream (100 ml)
Product Snapshot
Name: Solvane: Phytoplankton Rescue Cream
Format: 100 ml / 3.4 fl oz tube or airless pump (dieline provided)
Dieline attached:
Purpose & Key Benefits
Rescue dry or damaged skin—especially eczema & psoriasis.
All‑over use: hands, feet, elbows, knees, face, body.
Repairs barrier · Deep hydration · Calms irritation · Antioxidant shield.
Usage
Longevity: ~30 days when used daily on 10 in² of skin.
How: Apply pea‑size to clean, damp skin; massage ≥1 min; reapply as needed.
Ingredients
Label Ingredients:
Aloe Barbadensis (Aloe) Leaf Juice, Butyrospermum Parkii (Shea) Butter, Aqua (and) Propanediol (and) Nannochloropsis Gaditana (Phytoplankton) Extract, Simmondsia Chinensis (Jojoba) Seed Oil, Sodium Lactate, Cetyl Alcohol, Cetearyl Olivate (and) Sorbitan Olivate (Tesaril 400), Panthenol (Vitamin B5), Gluconolactone (and) Sodium
Benzoate (and) Calcium Gluconate (Corvex Prime), Illite (French Green Clay).
Look & Feel (for designer)
Minimal, ocean‑inspired, premium yet approachable. Off‑white base, deep‑teal accent, subtle algae texture.
Must‑Haves on Pack
Product name + “Rescue Cream” descriptor
Net weight (100 ml / 3.4 fl oz)
Tagline: “Reunite your skin with Earth’s base nutrition.”
Copy snippet: “Powered by sustainably grown phytoplankton.”
Icons: Vegan • Cruelty‑Free • Reef‑Safe • Recyclable
www.brimtidelabs.com

```html
<!DOCTYPE html>
<html lang="en">
<head>
<meta charset="utf-8">
<title>Solvane: Phytoplankton Rescue Cream — Label</title>
<link href="https://fonts.googleapis.com/css2?family=Oswald:wght@400;500&family=Lato:wght@400;700&display=swap" rel="stylesheet">
<style>
  :root{
    --page:#ffffff;
    --label-bg:#f8f6ee;
    --teal:#2f7190;
    --teal-deep:#264e63;
    --green:#5b9a35;
    --ink:#3a4650;
    --wave-teal:#cfe5e2;
    --wave-green:#dfe9cf;
  }
  *{margin:0;padding:0;box-sizing:border-box}
  html,body{width:750px;height:1200px;overflow:hidden;background:var(--page)}
  .canvas{position:relative;width:750px;height:1200px}
  .label{
    position:absolute;left:10px;top:527px;width:730px;height:146px;
    background:var(--label-bg);overflow:hidden;
    font-family:"Lato",sans-serif;color:var(--ink);
  }
  .texture{position:absolute;top:0;height:146px}
  .texture--left{left:0;width:130px;background:linear-gradient(90deg,rgba(207,229,226,0) 0%,var(--wave-teal) 60%,rgba(207,229,226,.2) 100%);opacity:.6}
  .texture--mid{left:300px;width:180px;background:linear-gradient(90deg,rgba(223,233,207,0) 0%,var(--wave-green) 45%,var(--wave-teal) 75%,rgba(207,229,226,0) 100%);opacity:.7}
  .brand{
    position:absolute;left:140px;top:126px;
    transform:rotate(-90deg);transform-origin:0 0;
    font-family:"Oswald",sans-serif;font-weight:500;font-size:29px;line-height:30px;
    letter-spacing:.5px;color:var(--teal);white-space:nowrap;
  }
  .product{position:absolute;left:184px;top:24px;width:106px}
  .product__kicker{font-family:"Lato",sans-serif;font-weight:700;font-size:10.6px;letter-spacing:.4px;color:var(--green);line-height:12px}
  .product__name{font-family:"Oswald",sans-serif;font-weight:400;font-size:17.5px;line-height:20px;color:var(--teal-deep);letter-spacing:.3px;white-space:nowrap}
  .tagline{
    margin-top:6px;height:11px;display:flex;align-items:center;justify-content:center;
    background:linear-gradient(90deg,var(--teal),var(--green));
    font-family:"Oswald",sans-serif;font-size:4.2px;letter-spacing:.45px;color:#fff;text-transform:uppercase;white-space:nowrap
  }
  .benefits{display:flex;gap:3px;margin-top:12px;list-style:none}
  .benefit{display:flex;align-items:center;gap:1.5px;font-size:3.4px;line-height:3.4px;font-weight:700;color:var(--teal)}
  .benefit svg{width:6px;height:6px;flex:none}
  .powered{margin-top:12px;font-size:4.8px;font-weight:700;color:var(--teal-deep);white-space:nowrap}
  .volume{margin-top:11px;font-size:5.5px;color:var(--teal-deep)}
  .details{position:absolute;left:484px;top:15px;width:200px;font-size:6.2px;line-height:8.3px;color:var(--ink)}
  .details__heading{font-family:"Oswald",sans-serif;font-size:7.6px;color:var(--green);margin-bottom:5px;white-space:nowrap}
  .details strong{font-weight:700;color:var(--teal-deep)}
  .details p{text-align:justify}
</style>
</head>
<body>
<main class="canvas">
  <section class="label" aria-label="Solvane Phytoplankton Rescue Cream jar label">
    <div class="texture texture--left" role="img" aria-label="Fine flowing algae line texture"></div>
    <div class="texture texture--mid" role="img" aria-label="Fine flowing algae line texture"></div>

    <div class="brand">SOLVANE</div>

    <div class="product">
      <div class="product__kicker">PHYTOPLANKTON</div>
      <div class="product__name">RESCUE CREAM</div>
      <div class="tagline">Restore your skin with Earth's base nutrition</div>
      <ul class="benefits">
        <li class="benefit"><svg viewBox="0 0 10 10" fill="none" stroke="currentColor" stroke-width=".9"><circle cx="5" cy="5" r="4"/><path d="M1.5 4h7M1.5 6h7"/></svg>Repairs<br>barrier</li>
        <li class="benefit"><svg viewBox="0 0 10 10" fill="none" stroke="currentColor" stroke-width=".9"><path d="M5 1C3 4 2.5 5.5 2.5 6.5a2.5 2.5 0 0 0 5 0C7.5 5.5 7 4 5 1z"/></svg>Deep<br>hydration</li>
        <li class="benefit"><svg viewBox="0 0 10 10" fill="none" stroke="currentColor" stroke-width=".9"><path d="M5 8.5C3 7 3 4 5 2c2 2 2 5 0 6.5zM5 8.5C3 8.5 1 7 1 4.5c2 0 3.5 1.5 4 4zM5 8.5c2 0 4-1.5 4-4-2 0-3.5 1.5-4 4z"/></svg>Calms<br>irritation</li>
        <li class="benefit"><svg viewBox="0 0 10 10" fill="none" stroke="currentColor" stroke-width=".9"><path d="M5 1l3.5 1.3v3C8.5 7.3 7 8.5 5 9.2 3 8.5 1.5 7.3 1.5 5.3v-3z"/><path d="M3.5 6.5C4 4.5 5.5 3.5 7 3.2"/></svg>Antioxidant<br>shield</li>
      </ul>
      <div class="powered">Powered By Sustainably Grown Phytoplankton</div>
      <div class="volume">100 ml / 3.4 fl oz</div>
    </div>

    <div class="details">
      <div class="details__heading">Rescue dry or damaged skin—especially eczema &amp; psoriasis.</div>
      <p>All-over use: hands, feet, elbows, knees, face, body.</p>
      <p><strong>Longevity:</strong> ~30 days when used daily on 10 in² of skin.</p>
      <p><strong>How:</strong> Apply pea-size to clean, damp skin; massage &ge;1 min; reapply as needed.</p>
      <p><strong>Ingredients:</strong> Aloe Barbadensis (Aloe) Leaf Juice, Butyrospermum Parkii (Shea) Butter, Aqua (and) Propanediol (and) Nannochloropsis Gaditana (Phytoplankton) Extract, Simmondsia Chinensis (Jojoba) Seed Oil, Sodium Lactate, Cetyl Alcohol, Cetearyl Olivate (and) Sorbitan Olivate (Tesaril 400), Panthenol (Vitamin B5), Gluconolactone (and) Sodium Benzoate (and) Calcium Gluconate (Corvex Prime), Illite (French Green Clay).</p>
    </div>
  </section>
</main>
</body>
</html>
```